table invoices in a modern format! (make it fun to look at!!)

Our has invoices that are shown to our clients. This is currently done in a normal table view, but its boring to look at and is not modern.
We would like to have a modern look and feel
it should ABSOLUTLY not be in table form.
Cards, graphs, pictures, whatever... should be fun and almost interactive.

the table file is how it current looks like.
the other two files were "ideas" to have a better representation
IT DOES NOT NEED TO LOOK LIKE THAT if you have a better idea please go for it.

secondary objective, the graphs/cards/whatever you design should be interactive, meaning I can "click on it" to pay a bill, or see more info.

Let me know if there are more questions!

```html
<!DOCTYPE html>
<html lang="en">
<head>
<meta charset="utf-8">
<title>Invoices Prior to 2019</title>
<link href="https://fonts.googleapis.com/css2?family=Lato:wght@400;700&family=Montserrat:wght@400;500&display=swap" rel="stylesheet">
<style>
:root{
  --blue:#1ea3f7;
  --green:#62d148;
  --red:#dc3545;
  --amber:#ffb414;
  --ink:#333;
  --muted:#555;
  --bg:#efefef;
  --card:#fff;
  --footer:#141414;
  --faint:#e9f3fb;
}
*{box-sizing:border-box;margin:0;padding:0}
html,body{width:813px;height:1200px;overflow:hidden}
body{background:var(--bg);font-family:'Lato',sans-serif;color:var(--ink);position:relative}
.page-header{height:72px;background:#fff;display:flex;align-items:center;justify-content:center}
.page-title{font-size:20px;font-weight:400;letter-spacing:.3px;color:#3a3a3a}
.year-bar{height:48px;background:var(--blue);display:flex;align-items:center;padding:0 100px}
.year-tab{width:49px;height:26px;display:flex;align-items:center;justify-content:center;color:#fff;font-weight:700;font-size:11.5px;margin-right:14px;border-radius:2px;text-decoration:none}
.year-tab.is-active{background:var(--green)}
.overview-btn{margin-left:auto;width:103px;height:26px;background:var(--green);color:#fff;font-weight:700;font-size:9px;display:flex;align-items:center;justify-content:center;border-radius:2px}
.summary{position:absolute;top:157px;left:101px;display:flex;gap:25px}
.summary-card{width:187px;height:91px;background:var(--card);border-radius:8px;box-shadow:0 3px 10px rgba(0,0,0,.08);display:flex;align-items:center;padding-left:22px;position:relative;overflow:hidden}
.summary-icon{width:46px;height:46px;border-radius:50%;background:var(--blue);display:flex;align-items:center;justify-content:center;flex:none}
.summary-text{margin-left:14px}
.summary-label{font-size:11px;font-weight:400;color:#222}
.summary-value{font-size:14px;font-weight:700;color:var(--blue);margin-top:4px}
.summary-ghost{position:absolute;right:-4px;bottom:-6px;opacity:.35}
.wallet-btn{position:absolute;top:275px;left:355px;width:103px;height:26px;background:var(--green);color:#fff;font-weight:700;font-size:9px;display:flex;align-items:center;justify-content:center;border-radius:2px;box-shadow:0 3px 6px rgba(0,0,0,.12)}
.invoice-grid{position:absolute;top:333px;left:101px;display:grid;grid-template-columns:repeat(3,187px);column-gap:26px;row-gap:34px}
.invoice-card{height:194px;background:var(--card);border-radius:8px;box-shadow:0 3px 10px rgba(0,0,0,.08);position:relative;overflow:hidden}
.invoice-head{height:50px;border-bottom:1px solid #e6e6e6;padding:12px 0 0 12px;position:relative}
.invoice-number{font-size:9.5px;color:#333}
.invoice-month{font-size:10.5px;font-weight:700;color:var(--blue);margin-top:6px;margin-left:1px}
.invoice-cal{position:absolute;right:11px;top:10px}
.invoice-rows{padding:15px 11px 0 0;display:grid;grid-template-columns:1fr 46px;column-gap:7px;row-gap:7px;align-items:center}
.row-label{text-align:right;font-size:8.3px;color:#333}
.row-value{text-align:right;font-size:10px;color:#333}
.balance-label{margin-top:4px}
.balance-chip{margin-top:4px;height:18px;border-radius:2px;color:#fff;font-size:10px;display:flex;align-items:center;justify-content:center;margin-left:-4px}
.chip-neg{background:var(--red)}
.chip-pos{background:var(--blue)}
.status{position:absolute;bottom:0;left:57px;width:74px;height:25px;border-radius:10px 10px 0 0;color:#fff;font-size:11px;display:flex;align-items:center;justify-content:center}
.status-paid{background:var(--green)}
.status-unpaid{background:var(--red)}
.status-partial{background:var(--amber)}
.site-footer{position:absolute;top:1053px;left:0;width:813px;height:147px;background:var(--footer);color:#eee;font-family:'Montserrat',sans-serif}
.footer-legal{text-align:center;font-size:9.5px;margin-top:46px}
.social{display:flex;justify-content:center;gap:6px;margin-top:22px}
.social-link{height:27px;padding:0 9px;border:1px solid #ddd;border-radius:14px;display:flex;align-items:center;font-size:8px;color:#fff}
</style>
</head>
<body>
<header class="page-header"><h1 class="page-title">INVOICES&nbsp; PRIOR TO 2019</h1></header>
<nav class="year-bar">
  <span class="year-tab is-active">2019</span>
  <span class="year-tab">2020</span>
  <span class="year-tab">2021</span>
  <span class="year-tab">2022</span>
  <span class="year-tab">2023</span>
  <span class="overview-btn">YEAR OVERVIEW</span>
</nav>

<section class="summary">
  <div class="summary-card">
    <div class="summary-icon"><svg width="26" height="22" viewBox="0 0 26 22" fill="none" stroke="#fff" stroke-width="1.3"><rect x="1" y="8" width="18" height="11" rx="1.5"/><line x1="1" y1="12" x2="19" y2="12"/><rect x="8" y="2" width="16" height="10" rx="1.5" transform="rotate(-20 16 7)"/><circle cx="21" cy="16" r="4"/></svg></div>
    <div class="summary-text"><div class="summary-label">PAYMENT:</div><div class="summary-value">€ 10651.94</div></div>
    <svg class="summary-ghost" width="56" height="42" viewBox="0 0 56 42" fill="none" stroke="#bfe0f7" stroke-width="2"><rect x="2" y="18" width="40" height="24" rx="3"/><rect x="20" y="2" width="32" height="20" rx="3" transform="rotate(-20 36 12)"/></svg>
  </div>
  <div class="summary-card">
    <div class="summary-icon"><svg width="20" height="26" viewBox="0 0 20 26" fill="none" stroke="#fff" stroke-width="1.3"><path d="M2 1h11l5 5v19H2z"/><line x1="5" y1="11" x2="15" y2="11"/><line x1="5" y1="15" x2="15" y2="15"/><line x1="5" y1="19" x2="15" y2="19"/><line x1="5" y1="6" x2="9" y2="6"/></svg></div>
    <div class="summary-text"><div class="summary-label">TOTAL PRICE:</div><div class="summary-value">€ 7849.08</div></div>
    <svg class="summary-ghost" width="46" height="34" viewBox="0 0 46 34" fill="none" stroke="#bfe0f7" stroke-width="2"><path d="M2 2h30l12 12v20H2z"/></svg>
  </div>
  <div class="summary-card">
    <div class="summary-icon"><svg width="26" height="24" viewBox="0 0 26 24" fill="none" stroke="#fff" stroke-width="1.3"><rect x="2" y="8" width="20" height="14" rx="2"/><rect x="5" y="2" width="12" height="6"/><rect x="16" y="12" width="8" height="6" rx="1"/></svg></div>
    <div class="summary-text"><div class="summary-label">BALANCE:</div><div class="summary-value">2802.86</div></div>
    <svg class="summary-ghost" width="50" height="34" viewBox="0 0 50 34" fill="none" stroke="#bfe0f7" stroke-width="2"><rect x="2" y="12" width="42" height="24" rx="3"/><rect x="10" y="2" width="22" height="10"/></svg>
  </div>
</section>

<span class="wallet-btn">MOVE TO WALLET</span>

<main class="invoice-grid">
  <article class="invoice-card">
    <div class="invoice-head"><div class="invoice-number">Number : TKZ19-0037</div><div class="invoice-month">JANUARY</div><svg class="invoice-cal" width="29" height="32" viewBox="0 0 29 32"><rect x="0" y="4" width="29" height="28" rx="3" fill="var(--faint)"/><rect x="6" y="0" width="3" height="7" fill="var(--faint)"/><rect x="20" y="0" width="3" height="7" fill="var(--faint)"/></svg></div>
    <div class="invoice-rows"><span class="row-label">Contract Price :</span><span class="row-value">€ 1152.00</span><span class="row-label">Extra After Credits</span><span class="row-value">€ 1248 00</span><span class="row-label">Payment Received</span><span class="row-value">€ 1243.20</span><span class="row-label balance-label">Open Balance</span><span class="balance-chip chip-neg">€ -141.18</span></div>
    <span class="status status-paid">PAID</span>
  </article>
  <article class="invoice-card">
    <div class="invoice-head"><div class="invoice-number">Number : TKZ19-0103</div><div class="invoice-month">FEBRUARY</div><svg class="invoice-cal" width="29" height="32" viewBox="0 0 29 32"><rect x="0" y="4" width="29" height="28" rx="3" fill="var(--faint)"/><rect x="6" y="0" width="3" height="7" fill="var(--faint)"/><rect x="20" y="0" width="3" height="7" fill="var(--faint)"/></svg></div>
    <div class="invoice-rows"><span class="row-label">Contract Price :</span><span class="row-value">€ 1152.00</span><span class="row-label">Extra After Credits</span><span class="row-value">€ 1248 00</span><span class="row-label">Payment Received</span><span class="row-value">€ 1243.20</span><span class="row-label balance-label">Open Balance</span><span class="balance-chip chip-pos">€ 91.20</span></div>
    <span class="status status-unpaid">UNPAID</span>
  </article>
  <article class="invoice-card">
    <div class="invoice-head"><div class="invoice-number">Number : TKZ19- 0355</div><div class="invoice-month">MARCH</div><svg class="invoice-cal" width="29" height="32" viewBox="0 0 29 32"><rect x="0" y="4" width="29" height="28" rx="3" fill="var(--faint)"/><rect x="6" y="0" width="3" height="7" fill="var(--faint)"/><rect x="20" y="0" width="3" height="7" fill="var(--faint)"/></svg></div>
    <div class="invoice-rows"><span class="row-label">Contract Price :</span><span class="row-value">€ 1152.00</span><span class="row-label">Extra After Credits</span><span class="row-value">€ 1248 00</span><span class="row-label">Payment Received</span><span class="row-value">€ 1243.20</span><span class="row-label balance-label">Open Balance</span><span class="balance-chip chip-pos">€ 59.86</span></div>
    <span class="status status-partial">PARTIAL</span>
  </article>
  <article class="invoice-card">
    <div class="invoice-head"><div class="invoice-number">Number : TKZ19-0354</div><div class="invoice-month">APRIL</div><svg class="invoice-cal" width="29" height="32" viewBox="0 0 29 32"><rect x="0" y="4" width="29" height="28" rx="3" fill="var(--faint)"/><rect x="6" y="0" width="3" height="7" fill="var(--faint)"/><rect x="20" y="0" width="3" height="7" fill="var(--faint)"/></svg></div>
    <div class="invoice-rows"><span class="row-label">Contract Price :</span><span class="row-value">€ 1152.00</span><span class="row-label">Extra After Credits</span><span class="row-value">€ 1248 00</span><span class="row-label">Payment Received</span><span class="row-value">€ 1243.20</span><span class="row-label balance-label">Open Balance</span><span class="balance-chip chip-pos">€ 0.00</span></div>
    <span class="status status-partial">PARTIAL</span>
  </article>
  <article class="invoice-card">
    <div class="invoice-head"><div class="invoice-number">Number : TKL19-0306</div><div class="invoice-month">MAY</div><svg class="invoice-cal" width="29" height="32" viewBox="0 0 29 32"><rect x="0" y="4" width="29" height="28" rx="3" fill="var(--faint)"/><rect x="6" y="0" width="3" height="7" fill="var(--faint)"/><rect x="20" y="0" width="3" height="7" fill="var(--faint)"/></svg></div>
    <div class="invoice-rows"><span class="row-label">Contract Price :</span><span class="row-value">€ 1152.00</span><span class="row-label">Extra After Credits</span><span class="row-value">€ 1248 00</span><span class="row-label">Payment Received</span><span class="row-value">€ 1243.20</span><span class="row-label balance-label">Open Balance</span><span class="balance-chip chip-neg">€ -141.18</span></div>
    <span class="status status-paid">PAID</span>
  </article>
  <article class="invoice-card">
    <div class="invoice-head"><div class="invoice-number">Number : TKL19-0398</div><div class="invoice-month">JUNE</div><svg class="invoice-cal" width="29" height="32" viewBox="0 0 29 32"><rect x="0" y="4" width="29" height="28" rx="3" fill="var(--faint)"/><rect x="6" y="0" width="3" height="7" fill="var(--faint)"/><rect x="20" y="0" width="3" height="7" fill="var(--faint)"/></svg></div>
    <div class="invoice-rows"><span class="row-label">Contract Price :</span><span class="row-value">€ 1152.00</span><span class="row-label">Extra After Credits</span><span class="row-value">€ 1248 00</span><span class="row-label">Payment Received</span><span class="row-value">€ 1243.20</span><span class="row-label balance-label">Open Balance</span><span class="balance-chip chip-neg">€ -141.18</span></div>
    <span class="status status-unpaid">UNPAID</span>
  </article>
  <article class="invoice-card">
    <div class="invoice-head"><div class="invoice-number">Number :&nbsp; TKL19-0479</div><div class="invoice-month">JULY</div><svg class="invoice-cal" width="29" height="32" viewBox="0 0 29 32"><rect x="0" y="4" width="29" height="28" rx="3" fill="var(--faint)"/><rect x="6" y="0" width="3" height="7" fill="var(--faint)"/><rect x="20" y="0" width="3" height="7" fill="var(--faint)"/></svg></div>
    <div class="invoice-rows"><span class="row-label">Contract Price :</span><span class="row-value">€ 1152.00</span><span class="row-label">Extra After Credits</span><span class="row-value">€ 1248 00</span><span class="row-label">Payment Received</span><span class="row-value">€ 1243.20</span><span class="row-label balance-label">Open Balance</span><span class="balance-chip chip-pos">€ 925.00</span></div>
    <span class="status status-paid">PAID</span>
  </article>
  <article class="invoice-card">
    <div class="invoice-head"><div class="invoice-number">Number : TKZ19-0037</div><div class="invoice-month">AUGUST</div><svg class="invoice-cal" width="29" height="32" viewBox="0 0 29 32"><rect x="0" y="4" width="29" height="28" rx="3" fill="var(--faint)"/><rect x="6" y="0" width="3" height="7" fill="var(--faint)"/><rect x="20" y="0" width="3" height="7" fill="var(--faint)"/></svg></div>
    <div class="invoice-rows"><span class="row-label">Contract Price :</span><span class="row-value">€ 1152.00</span><span class="row-label">Extra After Credits</span><span class="row-value">€ 1248 00</span><span class="row-label">Payment Received</span><span class="row-value">€ 1243.20</span><span class="row-label balance-label">Open Balance</span><span class="balance-chip chip-neg">€ -141.18</span></div>
    <span class="status status-unpaid">UNPAID</span>
  </article>
  <article class="invoice-card">
    <div class="invoice-head"><div class="invoice-number">Number :&nbsp; TKL19-0547</div><div class="invoice-month">SEPTEMBER</div><svg class="invoice-cal" width="29" height="32" viewBox="0 0 29 32"><rect x="0" y="4" width="29" height="28" rx="3" fill="var(--faint)"/><rect x="6" y="0" width="3" height="7" fill="var(--faint)"/><rect x="20" y="0" width="3" height="7" fill="var(--faint)"/></svg></div>
    <div class="invoice-rows"><span class="row-label">Contract Price :</span><span class="row-value">€ 1152.00</span><span class="row-label">Extra After Credits</span><span class="row-value">€ 1248 00</span><span class="row-label">Payment Received</span><span class="row-value">€ 1243.20</span><span class="row-label balance-label">Open Balance</span><span class="balance-chip chip-pos">€ 386.29</span></div>
    <span class="status status-paid">PAID</span>
  </article>
</main>

<footer class="site-footer">
  <p class="footer-legal">© 2019. All Rights Reserved | Privacy Policy | Terms and Conditions</p>
  <div class="social">
    <span class="social-link">Linkly</span>
    <span class="social-link">Chirpo</span>
    <span class="social-link">Vidzo</span>
    <span class="social-link">Snapo</span>
    <span class="social-link">Workin</span>
  </div>
</footer>
</body>
</html>
```